Training Company Needs a Web Design

We are a Training company that needs a website design completed for us. "The Harbor Loft" The website will be a 'community space' specialising in 'Change and Transformation'. It will be a 'space' where individuals can come to find out 'latest news', upcoming events and courses, chat with others and find 'tools and templates'. They will need to login as a 'Member'.

The final design needs to be professional but have a 'fun and interactive' feel and appeal to our target audience who are predominantly corporate individuals.

Target Market(s)

Corporate Individuals - they may have a Change or Project background

Industry/Entity Type

Business Consultant

Number of Pages Required

3 page

Font styles to use
Sans Serif

Requirements
Must have
• Design for 'Home Page'
• A professional and corporate 'feel' but be fun and interactive.
Nice to have
• A 'sense' of how some of the other pages may be designed or laid out.

```html
<!DOCTYPE html>
<html lang="en">
<head>
<meta charset="utf-8">
<title>The Harbor Loft</title>
<link href="https://fonts.googleapis.com/css2?family=Raleway:wght@300;400;500;600;700&family=Montserrat:wght@400;600;700&display=swap" rel="stylesheet">
<style>
:root{
  --teal:#47d9bf;
  --teal-dark:#32c4aa;
  --ink:#1c1c1c;
  --black:#000;
  --grey-bg:#f2f2f2;
  --text:#666;
  --line:#d8d8d8;
  --footer:#424242;
  --footer-dark:#262626;
  --white:#fff;
}
*{box-sizing:border-box;margin:0;padding:0}
html,body{width:766px;height:1200px;overflow:hidden}
body{position:relative;font-family:'Raleway',sans-serif;color:var(--text);background:var(--white)}
.abs{position:absolute}

/* header & hero */
.hero{left:0;top:0;width:766px;height:349px;background:linear-gradient(120deg,#3b3a35 0%,#6e6558 35%,#8b8577 55%,#4c4740 80%,#2a2826 100%)}
.hero-title{left:0;top:176px;width:766px;text-align:center;color:var(--white);text-shadow:0 1px 3px rgba(0,0,0,.5)}
.hero-title .strong{display:block;font-weight:700;font-size:22px;letter-spacing:-.2px}
.hero-title .light{display:block;font-weight:300;font-size:24px;margin-top:6px}
.navbar{left:195px;top:0;width:507px;height:31px;background:var(--teal)}
.navbar ul{list-style:none;display:flex;position:absolute;left:12px;top:11px}
.navbar li{font-family:'Montserrat',sans-serif;font-weight:600;font-size:8px;color:var(--white);letter-spacing:.3px;padding:0 12px;border-left:1px solid rgba(255,255,255,.45)}
.navbar li:first-child{border-left:none;padding-left:0}
.nav-btn{top:6px;height:20px;background:#eee;border:1px solid #ccc;font-family:'Montserrat',sans-serif;font-size:8px;color:#444;display:flex;align-items:center;gap:5px;padding:0 6px}
.nav-rule{left:195px;top:34px;width:507px;height:1px;background:rgba(255,255,255,.7)}
.logo-disc{left:65px;top:-15px;width:126px;height:126px;border-radius:50%;background:var(--white)}
.logo-mark{left:98px;top:18px;width:61px;height:66px;background:var(--teal);display:flex;align-items:center;justify-content:center;text-align:center;color:var(--white);font-weight:600;font-size:12px;line-height:14px}

/* services */
.services{left:0;top:349px;width:766px;height:224px;background:var(--grey-bg)}
.service{top:381px;width:160px;text-align:center}
.service .ring{width:76px;height:76px;margin:0 auto;border:1px solid #ccc;border-radius:50%;display:flex;align-items:center;justify-content:center}
.service h3{font-family:'Montserrat',sans-serif;font-weight:600;font-size:8.6px;color:#222;margin-top:11px;letter-spacing:.1px}
.service p{font-size:7.6px;line-height:10.8px;color:#777;margin-top:5px;padding:0 14px}
.service .more{display:block;margin-top:6px;font-family:'Montserrat',sans-serif;font-weight:600;font-size:7.4px;color:var(--teal)}

/* welcome & contact */
.split{left:0;top:573px}
.welcome h2{left:64px;top:590px;font-weight:400;font-size:21px;color:var(--white)}
.welcome .rule{left:64px;top:621px;width:335px;height:1px;background:#555}
.welcome .rule-accent{left:64px;top:620px;width:64px;height:2px;background:var(--teal)}
.welcome p{left:64px;top:630px;width:335px;font-size:8.8px;line-height:15.3px;color:#ddd;text-align:justify}
.btn-teal{background:var(--teal);color:var(--white);font-size:8.6px;display:flex;align-items:center;justify-content:center}
.contact h2{left:473px;top:602px;font-weight:300;font-size:21px;color:var(--white)}
.contact .rule{left:473px;top:634px;width:229px;height:1px;background:rgba(255,255,255,.6)}
.contact .rule-accent{left:473px;top:633px;width:44px;height:2px;background:#1c1c1c}
.field{left:474px;width:228px;background:var(--white);font-size:7.4px;color:#999;padding:9px 7px}
.submit-dark{left:474px;top:757px;width:69px;height:24px;background:#111;color:var(--white);font-family:'Montserrat',sans-serif;font-size:8.6px;display:flex;align-items:center;justify-content:center;gap:6px}

/* events & news */
.section-title{top:837px;font-weight:400;font-size:21px;color:#222;display:flex;align-items:center;gap:8px}
.hr{height:1px;background:var(--line)}
.event-thumb{left:63px;width:76px;height:49px;border:2px solid #ddd;background:linear-gradient(135deg,#c9d3da,#8e9ba5 60%,#5b6670)}
.event h4,.news h4{font-family:'Montserrat',sans-serif;font-weight:600;color:#222}
.event h4{font-size:10.8px}
.event p{font-size:8px;line-height:13.5px;color:#444;margin-top:2px}
.meta{display:flex;align-items:center;gap:4px;font-size:6.4px;color:#555;margin-top:4px}
.meta .sep{width:1px;height:9px;background:#bbb;margin:0 5px}
.date-badge{left:410px;width:32px;height:36px;border:1px solid #ccc;background:var(--white);text-align:center}
.date-badge .d{background:var(--teal);color:var(--white);font-family:'Montserrat',sans-serif;font-weight:700;font-size:6.6px;height:15px;line-height:15px}
.date-badge .y{font-family:'Montserrat',sans-serif;font-weight:700;font-size:9.5px;color:#222;line-height:19px}
.news h4{font-size:8.4px}
.news p{font-size:8.4px;line-height:14px;color:#555;margin-top:3px}
.news .more{font-family:'Montserrat',sans-serif;font-weight:600;font-size:6.4px;color:var(--teal);margin-top:2px}

/* footer */
.footer{left:0;top:1048px;width:766px;height:128px;background:var(--footer)}
.map{left:64px;top:1067px;width:170px;height:91px;border:2px solid #ddd;background:linear-gradient(135deg,#e8e4da,#d9e3c8 40%,#b9d2e6 70%,#e8e4da)}
.addr{left:256px;color:#eee;font-size:7.4px;line-height:9.5px}
.addr strong{font-family:'Montserrat',sans-serif;font-weight:700;font-size:7.4px}
.row{display:flex;align-items:flex-start;gap:8px}
.row svg{flex:none;margin-top:1px}
.stay h5{left:422px;top:1066px;font-weight:400;font-size:10.4px;color:#eee}
.stay .email{left:422px;top:1086px;width:126px;height:17px;border:1px solid #ddd;font-size:6.4px;color:#ccc;padding:4px 5px}
.stay .go{left:422px;top:1110px;width:126px;height:19px;font-family:'Montserrat',sans-serif;font-weight:700;font-size:7.6px;border:1px solid #fff}
.stay p{left:422px;top:1140px;width:130px;font-size:6.2px;line-height:7.6px;color:#ddd}
.foot-logo{left:606px;top:1070px;width:47px;height:50px;background:var(--teal);border:2px solid #6ce6d0;display:flex;align-items:center;justify-content:center;text-align:center;color:var(--white);font-weight:600;font-size:9px;line-height:10.5px}
.social{left:588px;top:1141px;display:flex;gap:8px}
.social span{width:12px;height:12px;background:#8a8a8a}
.copy{left:0;top:1176px;width:766px;height:24px;background:var(--teal);color:#1f4f47;font-size:7.4px;display:flex;align-items:center;justify-content:center}
</style>
</head>
<body>

<!-- Hero -->
<div class="abs hero" role="img" aria-label="Photo of business people smiling in a meeting"></div>
<h1 class="abs hero-title"><span class="strong">We Specialising In</span><span class="light">Change And Transformation</span></h1>

<nav class="abs navbar">
  <ul><li>HOME</li><li>ABOUT US</li><li>COURSES</li><li>EVENTS</li><li>NEWS</li><li>CONTACT US</li></ul>
</nav>
<div class="abs nav-btn" style="left:579px;width:51px">
  <svg width="9" height="8" viewBox="0 0 9 8"><path d="M0 3h4V1l3 3-3 3V5H0z" fill="#333"/><path d="M6 0h3v8H6" fill="none" stroke="#333"/></svg>LOGIN</div>
<div class="abs nav-btn" style="left:634px;width:64px">
  <svg width="10" height="8" viewBox="0 0 10 8"><path d="M1 1h6v4H3L1 7z" fill="none" stroke="#333"/><path d="M7 3h2v3L8 7V6H5" fill="none" stroke="#333"/></svg>LIVE CHAT</div>
<div class="abs nav-rule"></div>
<div class="abs logo-disc"></div>
<div class="abs logo-mark">THE<br>HARBOR<br>LOFT</div>

<!-- Services -->
<section class="abs services"></section>
<svg class="abs" style="left:40px;top:448px" width="16" height="26"><path d="M14 1L2 13l12 12" fill="none" stroke="#c8c8c8" stroke-width="2"/></svg>
<svg class="abs" style="left:710px;top:448px" width="16" height="26"><path d="M2 1l12 12L2 25" fill="none" stroke="#c8c8c8" stroke-width="2"/></svg>

<div class="abs service" style="left:58px">
  <div class="ring"><svg width="36" height="34" viewBox="0 0 36 34" fill="#222"><rect x="13" y="1" width="10" height="8"/><path d="M18 9v6M6 15h24M6 15v4M18 15v4M30 15v4" stroke="#222" stroke-width="1.6" fill="none"/><rect x="1" y="20" width="10" height="8"/><rect x="13" y="20" width="10" height="8"/><rect x="25" y="20" width="10" height="8"/></svg></div>
  <h3>MANAGEMENT TRAINING</h3>
  <p>Lorem ipsum dolor sit amet, consectetuer adipiscing elit, sed augue duis dol facilisi.</p>
  <span class="more">READ MORE »</span>
</div>
<div class="abs service" style="left:225px">
  <div class="ring"><svg width="30" height="34" viewBox="0 0 30 34" fill="#222"><circle cx="15" cy="11" r="7" fill="none" stroke="#222" stroke-width="2"/><rect x="12" y="18" width="6" height="4"/><path d="M15 0v2M4 4l2 2M26 4l-2 2M1 12h2M27 12h2" stroke="#222" stroke-width="1.6"/><path d="M4 34l2-8h18l2 8z"/></svg></div>
  <h3>BUSINESS VALUATION</h3>
  <p>Lorem ipsum dolor sit amet, consectetuer adipiscing elit, sed augue duis te facilisi.</p>
  <span class="more">READ MORE »</span>
</div>
<div class="abs service" style="left:385px">
  <div class="ring"><svg width="38" height="32" viewBox="0 0 38 32"><rect x="1" y="1" width="36" height="23" fill="none" stroke="#222" stroke-width="2"/><path d="M14 24l-2 6h14l-2-6" fill="#222"/><rect x="7" y="15" width="3" height="6" fill="#222"/><rect x="12" y="12" width="3" height="9" fill="#222"/><rect x="17" y="13" width="3" height="8" fill="#222"/><rect x="22" y="9" width="3" height="12" fill="#222"/><rect x="27" y="6" width="3" height="15" fill="#222"/><path d="M6 12l8-5 6 3 11-6" fill="none" stroke="#222" stroke-width="1.4"/></svg></div>
  <h3>BUSINESS ANALYSIS</h3>
  <p>Lorem ipsum dolor sit amet, consectetuer adipiscing elit, sed duis dolore te facilisi.</p>
  <span class="more">READ MORE »</span>
</div>
<div class="abs service" style="left:546px">
  <div class="ring"><svg width="30" height="34" viewBox="0 0 30 34" fill="#222"><path d="M8 2v30M8 3l14 4-14 5" fill="#222" stroke="#222" stroke-width="2"/><rect x="3" y="30" width="24" height="3"/></svg></div>
  <h3>EXIT STRATEGY PLANNING</h3>
  <p>Lorem ipsum dolor sit amet, consectetuer adipiscing elit, sed duis dolore te facilisi.</p>
  <span class="more">READ MORE »</span>
</div>

<!-- Welcome / Quick contact -->
<svg class="abs split" width="766" height="230" viewBox="0 0 766 230">
  <polygon points="0,0 462,0 371,216 0,216" fill="#000"/>
  <polygon points="462,13 766,13 766,229 366,229" fill="#47d9bf"/>
</svg>
<div class="welcome">
  <h2 class="abs">Welcome To The Harbor Loft</h2>
  <div class="abs rule"></div><div class="abs rule-accent"></div>
  <p class="abs">Lorem ipsum dolor sit amet, consectetuer adipiscing elit, sed diam nonummy nibh euismod tincidunt ut laoreet dolore magna aliquam erat volutpat. Ut wisi enim ad minim veniam, quis nostrud exerci tation ullamcorper suscipit lobortis nisl ut aliquip ex ea commodo consequat. Duis autem vel eum iriure dolor in hendrerit in vulputate velit esse molestie consequat, vel illum dolore eu feugiat nulla facilisis at vero eros et accumsan et iusto odio dignissim qui blandit praesent luptatum augue duis dolore te feugait nulla facilisi.</p>
  <div class="abs btn-teal" style="left:62px;top:746px;width:77px;height:24px">Read More</div>
</div>
<div class="contact">
  <h2 class="abs">Quick Contact</h2>
  <div class="abs rule"></div><div class="abs rule-accent"></div>
  <div class="abs field" style="top:645px;height:24px">Your Name</div>
  <div class="abs field" style="top:674px;height:24px">Your Email</div>
  <div class="abs field" style="top:705px;height:43px">Message</div>
  <div class="abs submit-dark">SUBMIT <svg width="12" height="7" viewBox="0 0 12 7"><path d="M0 3.5h10M7 .5l3 3-3 3" fill="none" stroke="#fff" stroke-width="1.4"/></svg></div>
</div>

<!-- Upcoming events -->
<h2 class="abs section-title" style="left:64px">
  <svg width="17" height="17" viewBox="0 0 17 17"><rect x="1" y="3" width="15" height="13" fill="none" stroke="#222" stroke-width="1.6"/><rect x="1" y="3" width="15" height="3" fill="#222"/><path d="M5 1v4M12 1v4" stroke="#222" stroke-width="1.6"/><path d="M4 9h9M4 12h9M7 7v8M10 7v8" stroke="#222" stroke-width=".8"/></svg>
  Upcoming Events</h2>
<div class="abs hr" style="left:64px;top:865px;width:290px"></div>

<div class="abs event-thumb" style="top:881px" role="img" aria-label="Photo of a team in a training session"></div>
<div class="abs event" style="left:149px;top:878px;width:205px">
  <h4>Oatmeal Apples &amp; Almonds</h4>
  <p>Lorem ipsum dolor sit amet ectuer adipiscing laoreet dore mgna aliquam volutpat.</p>
  <div class="meta"><svg width="8" height="8" viewBox="0 0 8 8" fill="#444"><circle cx="4" cy="2.3" r="2"/><path d="M0 8c0-3 8-3 8 0z"/></svg>Published By: Morrow<span class="sep"></span><svg width="8" height="8" viewBox="0 0 8 8"><rect x=".5" y=".5" width="7" height="7" fill="none" stroke="#444"/><path d="M2 3h4M2 5h4" stroke="#444" stroke-width=".8"/></svg> 14 Feb<span class="sep"></span><svg width="8" height="7" viewBox="0 0 8 7" fill="#222"><ellipse cx="4" cy="3" rx="4" ry="3"/><path d="M1 5l-1 2 3-1z"/></svg> 0</div>
</div>
<div class="abs hr" style="left:149px;top:944px;width:205px;background:#e6e6e6"></div>

<div class="abs event-thumb" style="top:954px" role="img" aria-label="Photo of a presenter with a seated group"></div>
<div class="abs event" style="left:149px;top:951px;width:205px">
  <h4>Oatmeal Apples &amp; Almonds</h4>
  <p>Lorem ipsum dolor sit amet ectuer adipiscing laoreet dore mgna aliquam volutpat.</p>
  <div class="meta"><svg width="8" height="8" viewBox="0 0 8 8" fill="#444"><circle cx="4" cy="2.3" r="2"/><path d="M0 8c0-3 8-3 8 0z"/></svg>Published By: Morrow<span class="sep"></span><svg width="8" height="8" viewBox="0 0 8 8"><rect x=".5" y=".5" width="7" height="7" fill="none" stroke="#444"/><path d="M2 3h4M2 5h4" stroke="#444" stroke-width=".8"/></svg> 14 Feb<span class="sep"></span><svg width="8" height="7" viewBox="0 0 8 7" fill="#222"><ellipse cx="4" cy="3" rx="4" ry="3"/><path d="M1 5l-1 2 3-1z"/></svg> 0</div>
</div>

<div class="abs" style="left:381px;top:840px;width:1px;height:184px;background:#e2e2e2"></div>

<!-- Latest news -->
<h2 class="abs section-title" style="left:410px">
  <svg width="18" height="16" viewBox="0 0 18 16" fill="#222"><path d="M1 5h4l9-4v14L5 11H1z"/><path d="M4 11l2 5h2l-1-5z"/></svg>
  Latest News</h2>
<div class="abs hr" style="left:409px;top:865px;width:293px"></div>

<div class="abs date-badge" style="top:881px"><div class="d">23 FEB</div><div class="y">2016</div></div>
<div class="abs news" style="left:452px;top:879px;width:250px">
  <h4>Lorem Ipsum Dolor Sit Amet Consectetuer</h4>
  <p>Cdipiscing elit sed diam nmy nibod tincidunlt utrlaoreet elit sed dolore magna aliquam.</p>
  <div class="more">READ MORE »</div>
</div>
<div class="abs hr" style="left:409px;top:942px;width:283px;background:#e6e6e6"></div>

<div class="abs date-badge" style="top:954px"><div class="d">23 FEB</div><div class="y">2016</div></div>
<div class="abs news" style="left:452px;top:954px;width:250px">
  <h4>Lorem Ipsum Dolor Sit Amet Consectetuer</h4>
  <p>Cdipiscing elit sed diam nonmmy nibod tinnlt utllaoreet elit dolore magna aliquam.</p>
  <div class="more">READ MORE »</div>
</div>

<!-- Footer -->
<footer class="abs footer"></footer>
<div class="abs map" role="img" aria-label="Street map showing the office location"></div>

<div class="abs addr" style="top:1066px">
  <div class="row"><svg width="9" height="12" viewBox="0 0 9 12" fill="#fff"><path d="M4.5 0a4.5 4.5 0 00-4.5 4.5C0 8 4.5 12 4.5 12S9 8 9 4.5A4.5 4.5 0 004.5 0zm0 6.3a1.8 1.8 0 110-3.6 1.8 1.8 0 010 3.6z"/></svg>
  <div style="margin-left:7px"><strong>THE HARBOR LOFT</strong><br>Pier Road no 48<br>near harbour walk<br>Zip:20417</div></div>
</div>
<div class="abs addr" style="top:1108px"><div class="row"><svg width="10" height="10" viewBox="0 0 10 10" fill="#fff"><path d="M2 0l2 2.5-1.2 1.5c.7 1.4 1.8 2.5 3.2 3.2L7.5 6 10 8 8.5 10C4 10 0 6 0 1.5z"/></svg><span style="margin-left:6px">555 0148 2210</span></div></div>
<div class="abs addr" style="top:1127px"><div class="row"><svg width="10" height="10" viewBox="0 0 10 10" fill="#fff"><rect x="2" y="0" width="6" height="3"/><rect x="0" y="3.5" width="10" height="4"/><rect x="2" y="7" width="6" height="3" fill="none" stroke="#fff"/></svg><span style="margin-left:6px">555 0148 2211</span></div></div>
<div class="abs addr" style="top:1145px"><div class="row"><svg width="11" height="8" viewBox="0 0 11 8"><rect x=".5" y=".5" width="10" height="7" fill="none" stroke="#fff"/><path d="M.5.5l5 4 5-4M.5 7.5l4-3.5M10.5 7.5l-4-3.5" fill="none" stroke="#fff"/></svg><span style="margin-left:5px">info@theharborloft.com</span></div></div>

<svg class="abs" style="left:392px;top:1048px" width="178" height="128" viewBox="0 0 178 128"><polygon points="19,0 178,0 160,128 0,128" fill="#262626"/></svg>
<div class="stay">
  <h5 class="abs">Stay in Touch</h5>
  <div class="abs email">Enter your email....</div>
  <div class="abs btn-teal go">SUBMIT</div>
  <p class="abs">We never Share your email address with another third party.</p>
</div>

<div class="abs foot-logo">THE<br>HARBOR<br>LOFT</div>
<div class="abs social" aria-label="Social links">
  <span></span><span></span><span></span><span></span><span></span>
</div>

<div class="abs copy">© 2016 Theharborloft. All Rights Reserved</div>
</body>
</html>
```